ebook cover for first in a light hearted series of Bright Routine Manuals

My project is a short (8,000 word) ebook The cover needs to include a logo with the words “The Bright Routine Manual”, as this is the first of a series and I want to have a common logo across the different books in the series. The logo also needs to be square so that I can use it as the logo for my podcasts. Something similar to the attached could work, but I am open to ideas:Then, underneath the logo I need the title of the specific book in the series; in this case ‘On Moving With A Partner Abroad’.In addition, I would like a subtitle on the cover saying ‘Easy to Implement Habits to Help You Make the Most of Expat Life.’One or more cover images could be added based on the themes from the chapter headings as below:Chapter Headings are as follows1. Turn up2. Share Your Umbrella3. Do What You Have Always Wanted4. Keep Up and Keep at It5. Use Your Hands6. Pay Attention7. Take The Bus
This is not a traditional self- help book. It features personal stories

Target Market(s)

Expat Women

Font styles to use
Serif
Sans Serif

Colors

Designer to choose colors to be used in the design.

Requirements
Must have
• A warm and whimsical feel
Should not have
• A corporate feel

```html
<!DOCTYPE html>
<html lang="en">
<head>
<meta charset="utf-8">
<title>On Moving With A Partner Abroad — ebook cover</title>
<link rel="stylesheet" href="https://fonts.googleapis.com/css2?family=Oswald:wght@400;500&family=PT+Serif:wght@400;700&family=Open+Sans:ital,wght@1,300;1,700&display=swap">
<style>
  :root {
    --stage: #c9d0d2;
    --sky-top: #5f8fcf;
    --sky-mid: #8fb3e2;
    --sun-yellow: #f6c30a;
    --umbrella: #f7b800;
    --paper: #ffffff;
    --title-yellow: #f4b400;
    --title-orange: #f08a00;
    --ink: #141414;
  }
  * { margin: 0; padding: 0; box-sizing: border-box; }
  html, body {
    width: 1200px;
    height: 989px;
    overflow: hidden;
    background: var(--stage);
  }
  .stage {
    position: relative;
    width: 1200px;
    height: 989px;
    display: flex;
    align-items: center;
    justify-content: center;
  }
  .cover {
    position: relative;
    width: 630px;
    height: 935px;
    background: var(--paper);
    overflow: hidden;
    box-shadow: 0 10px 30px rgba(0,0,0,0.18);
  }
  .cover-photo {
    position: absolute;
    inset: 0 0 auto 0;
    height: 720px;
    background:
      radial-gradient(ellipse 60% 45% at 55% 0%, var(--umbrella) 0 55%, rgba(247,184,0,0) 56%),
      radial-gradient(ellipse 40% 30% at 100% 8%, #fff6b0 0, rgba(255,246,176,0) 70%),
      linear-gradient(180deg, var(--sky-top) 0%, var(--sky-mid) 55%, #e9f0fa 82%, var(--paper) 100%);
  }
  .series-mark {
    position: absolute;
    top: 32px;
    right: 52px;
    display: flex;
    align-items: center;
    gap: 8px;
  }
  .series-mark__square {
    width: 14px;
    height: 14px;
    border: 2px solid var(--ink);
  }
  .series-mark__name {
    font-family: 'Oswald', sans-serif;
    font-weight: 400;
    font-size: 20px;
    line-height: 1.05;
    color: var(--ink);
    width: 110px;
  }
  .subtitle {
    position: absolute;
    top: 384px;
    right: 50px;
    width: 250px;
    text-align: center;
    font-family: 'Open Sans', sans-serif;
    font-style: italic;
    font-weight: 300;
    font-size: 18px;
    line-height: 1.35;
    color: var(--paper);
  }
  .subtitle strong { font-weight: 700; }
  .title {
    position: absolute;
    top: 560px;
    left: 0;
    right: 0;
    text-align: center;
    font-family: 'PT Serif', serif;
    line-height: 0.95;
  }
  .title__lead {
    display: block;
    font-weight: 400;
    font-size: 96px;
    color: var(--title-yellow);
    letter-spacing: -2px;
  }
  .title__lead small {
    font-size: 48px;
    color: var(--title-orange);
    letter-spacing: 0;
  }
  .title__rest {
    display: block;
    margin-top: 6px;
    font-weight: 700;
    font-size: 46px;
    color: var(--title-orange);
    letter-spacing: -1px;
  }
  .author {
    position: absolute;
    bottom: 72px;
    left: 0;
    right: 0;
    text-align: center;
    font-family: 'Oswald', sans-serif;
    font-weight: 500;
    font-size: 34px;
    letter-spacing: 16px;
    color: var(--ink);
  }
</style>
</head>
<body>
<main class="stage">
  <article class="cover">
    <div class="cover-photo" role="img" aria-label="Photograph of a bright yellow beach umbrella against a blue sky with white clouds, fading to white"></div>

    <div class="series-mark">
      <span class="series-mark__square"></span>
      <span class="series-mark__name">The Bright Routine Manual</span>
    </div>

    <p class="subtitle"><strong>Easy</strong> to Implement Habits to Help You Make the Most of <strong>Expat Life</strong></p>

    <h1 class="title">
      <span class="title__lead"><small>On</small> Moving</span>
      <span class="title__rest">With A Partner Abroad</span>
    </h1>

    <p class="author">AUTHOR NAME</p>
  </article>
</main>
</body>
</html>
```